Harlan Ridge Smokehouse Jamboree's 10th ever event needs a Poster! This Non-Profit is a blast

We need a totally NEW and FUN poster design to promote our tiny Kentucky town which hosts 40,000+ people who come to meet the TV Celebrity BBQ Pitmasters - who smoke meat for their fans. It is all about Beers, Bands, BBQ + Bourbon. We are a family event with Free music all weekend long.

Target Market(s)

People who love Beer, BBQ, Bands and Bourbon

Colors
ec1f27
0555a3

Requirements
Must have
• Please only use original art.
• High energy / Fresh / Young
• Name: Harlan Ridge Smokehouse Jamboree
• 10th ever
• Sept 4+5, 2020
• Bands, Beer, BBQ + Bourbon
• Hosted by: Copperfield Hollow Distillery
• 2817 Marlow Pike Ashby, KY 40198
• $5 admission - FREE MUSIC - FREE Parking
Nice to have
• Please only use original art. Trademarked images and logos will be rejected.

```html
<!DOCTYPE html>
<html lang="en">
<head>
<meta charset="utf-8">
<title>Harlan Ridge Smokehouse Jamboree – Poster</title>
<link href="https://fonts.googleapis.com/css2?family=Lilita+One&family=Montserrat:wght@700;800;900&display=swap" rel="stylesheet">
<style>
  :root {
    --fest-red: #ec1f27;
    --deep-red: #a3121a;
    --fest-blue: #0555a3;
    --sky-blue: #2a9be0;
    --light-blue: #5fb3ea;
    --navy: #10175c;
    --yellow: #f7f21c;
    --gold: #ffd23a;
    --flame: #f57a12;
    --white: #ffffff;
    --ink: #1a1a1a;
    --pig: #f2d3b0;
    --pig-shade: #d9b48c;
    --overalls: #6f7b8c;
    --mat: #000000;
  }
  * { box-sizing: border-box; margin: 0; padding: 0; }
  html, body {
    width: 955px; height: 1200px; overflow: hidden;
    background: var(--mat);
  }
  .poster {
    position: absolute; left: 105px; top: 113px;
    width: 740px; height: 962px; overflow: hidden;
    background: radial-gradient(ellipse at 50% 48%, #7fd0ff 0%, var(--sky-blue) 30%, var(--fest-blue) 70%, var(--navy) 100%);
    font-family: "Montserrat", sans-serif;
  }
  .bunting {
    position: absolute; left: 0; top: 0; width: 740px; height: 200px;
    background: linear-gradient(180deg, rgba(236,31,39,.55) 0%, rgba(255,255,255,.4) 40%, rgba(5,85,163,.55) 100%);
    clip-path: polygon(0 30%, 30% 0, 70% 0, 100% 55%, 100% 70%, 65% 20%, 35% 20%, 0 100%);
  }
  .fireworks {
    position: absolute; border-radius: 50%;
    background: radial-gradient(circle, rgba(255,255,255,.75) 0%, rgba(255,255,255,.2) 35%, transparent 70%);
  }
  .fireworks--left { left: 30px; top: 220px; width: 230px; height: 230px; }
  .fireworks--right { left: 570px; top: 110px; width: 180px; height: 180px; }
  .guitar {
    position: absolute; left: 545px; top: 190px; width: 90px; height: 470px;
    background: linear-gradient(200deg, rgba(200,235,255,.35), rgba(200,235,255,.08));
    transform: rotate(22deg); border-radius: 40px;
  }
  .title { position: absolute; left: 0; width: 740px; text-align: center; font-family: "Lilita One", sans-serif; }
  .title__top {
    top: 42px; font-size: 54px; color: var(--white); letter-spacing: 1px;
    -webkit-text-stroke: 3px var(--fest-blue); paint-order: stroke fill;
    text-shadow: 0 4px 0 var(--navy);
  }
  .title__main {
    top: 120px; font-size: 98px; line-height: 1; color: var(--fest-red);
    -webkit-text-stroke: 6px var(--white); paint-order: stroke fill;
    text-shadow: 6px 7px 0 var(--navy);
  }
  .title__sub {
    top: 240px; font-size: 68px; line-height: 1; color: var(--light-blue);
    -webkit-text-stroke: 5px var(--fest-red); paint-order: stroke fill;
    text-shadow: 4px 5px 0 var(--navy);
  }
  .ribbon { position: absolute; left: 200px; top: 320px; width: 340px; height: 80px; }
  .ribbon__text {
    position: absolute; left: 0; top: 327px; width: 740px; text-align: center;
    font-family: "Lilita One", sans-serif; font-size: 34px; line-height: 1; color: var(--yellow);
    -webkit-text-stroke: 2px var(--ink); paint-order: stroke fill;
  }
  .pig {
    position: absolute; left: 175px; top: 375px; width: 380px; height: 360px;
    border-radius: 48% 48% 30% 30% / 55% 55% 20% 20%;
    border: 3px solid rgba(26,26,26,.55);
    background:
      radial-gradient(ellipse 38% 30% at 42% 42%, #e8b99a 0%, transparent 100%),
      linear-gradient(180deg, var(--pig) 0%, var(--pig) 45%, var(--pig-shade) 60%, var(--overalls) 72%, #55606f 100%);
  }
  .flames {
    position: absolute; left: 0; top: 450px; width: 740px; height: 280px;
    background: linear-gradient(180deg, rgba(245,122,18,0) 0%, rgba(245,122,18,.55) 40%, rgba(245,122,18,.9) 65%, var(--gold) 100%);
  }
  .badge {
    position: absolute; border-radius: 50%; background: var(--white);
    border: 6px solid var(--fest-blue); box-shadow: 0 0 0 5px var(--navy), 0 0 0 8px var(--white);
    display: flex; flex-direction: column; align-items: center; justify-content: center;
    text-align: center; font-weight: 900; color: var(--fest-red);
  }
  .badge--admission { left: 64px; top: 486px; width: 132px; height: 132px; }
  .badge--admission .badge__price { font-size: 36px; line-height: 1; }
  .badge--admission .badge__label { font-size: 14px; }
  .badge--free { left: 546px; top: 408px; width: 148px; height: 148px; font-size: 15px; line-height: 1.25; }
  .badge__stars { color: var(--fest-blue); font-size: 9px; letter-spacing: 4px; }
  .zigzag { position: absolute; left: 0; top: 710px; width: 740px; height: 20px; }
  .band { position: absolute; left: 0; width: 740px; display: flex; align-items: center; justify-content: center; white-space: nowrap; }
  .band--date { top: 728px; height: 78px; background: var(--fest-red); color: var(--white); font-size: 48px; font-weight: 800; gap: 20px; }
  .flame-icon { width: 44px; height: 44px; }
  .band--acts { top: 806px; height: 52px; background: var(--navy); color: var(--white); font-size: 30px; font-weight: 900; letter-spacing: .5px; gap: 8px; }
  .band--acts .star { color: var(--yellow); font-size: 16px; }
  .band--host { top: 858px; height: 37px; background: var(--yellow); color: var(--fest-red); font-size: 22px; font-weight: 800; }
  .band--address { top: 895px; height: 67px; background: var(--fest-red); color: var(--white); font-size: 28px; font-weight: 700; }
</style>
</head>
<body>
<main class="poster">
  <div class="bunting" role="img" aria-label="Stars-and-stripes bunting hanging across the top"></div>
  <div class="fireworks fireworks--left" role="img" aria-label="White firework burst"></div>
  <div class="fireworks fireworks--right" role="img" aria-label="White firework burst"></div>
  <div class="guitar" role="img" aria-label="Faint outline of an electric guitar"></div>

  <h1>
    <div class="title title__top">HARLAN RIDGE</div>
    <div class="title title__main">SMOKEHOUSE</div>
    <div class="title title__sub">JAMBOREE</div>
  </h1>

  <svg class="ribbon" viewBox="0 0 340 80" aria-hidden="true">
    <polygon points="0,30 40,30 40,70 20,50 0,70" fill="var(--deep-red)"/>
    <polygon points="340,30 300,30 300,70 320,50 340,70" fill="var(--deep-red)"/>
    <path d="M30,18 Q170,-2 310,18 L310,60 Q170,40 30,60 Z" fill="var(--fest-red)" stroke="var(--white)" stroke-width="2"/>
    <text x="50" y="45" fill="#fff" font-size="16">★</text>
    <text x="276" y="45" fill="#fff" font-size="16">★</text>
  </svg>
  <div class="ribbon__text">10th ever</div>

  <div class="pig" role="img" aria-label="Cartoon pig mascot in grey overalls, eyes closed, hugging its belly"></div>
  <div class="flames" role="img" aria-label="Wall of orange barbecue flames"></div>

  <div class="badge badge--admission">
    <span class="badge__stars">★★★</span>
    <span class="badge__price">$5</span>
    <span class="badge__label">ADMISSION</span>
    <span class="badge__stars">★★★</span>
  </div>
  <div class="badge badge--free">
    <span class="badge__stars">★★★</span>
    <span>FREE MUSIC<br>FREE PARKING</span>
    <span class="badge__stars">★★★</span>
  </div>

  <svg class="zigzag" viewBox="0 0 740 20" preserveAspectRatio="none" aria-hidden="true">
    <polygon fill="var(--fest-red)" points="0,20 0,8 12,0 24,8 36,0 48,8 60,0 72,8 84,0 96,8 108,0 120,8 132,0 144,8 156,0 168,8 180,0 192,8 204,0 216,8 228,0 240,8 252,0 264,8 276,0 288,8 300,0 312,8 324,0 336,8 348,0 360,8 372,0 384,8 396,0 408,8 420,0 432,8 444,0 456,8 468,0 480,8 492,0 504,8 516,0 528,8 540,0 552,8 564,0 576,8 588,0 600,8 612,0 624,8 636,0 648,8 660,0 672,8 684,0 696,8 708,0 720,8 732,0 740,6 740,20"/>
  </svg>

  <div class="band band--date">
    <svg class="flame-icon" viewBox="0 0 36 36" aria-hidden="true"><path d="M18 2 C24 12 32 16 30 25 A12 11 0 0 1 6 25 C4 17 12 12 18 2 Z" fill="var(--flame)"/><path d="M18 14 C22 20 25 22 24 27 A6 6 0 0 1 12 27 C11 22 15 20 18 14 Z" fill="var(--gold)"/></svg>
    <span>Sept 4+5, 2020</span>
    <svg class="flame-icon" viewBox="0 0 36 36" aria-hidden="true"><path d="M18 2 C24 12 32 16 30 25 A12 11 0 0 1 6 25 C4 17 12 12 18 2 Z" fill="var(--flame)"/><path d="M18 14 C22 20 25 22 24 27 A6 6 0 0 1 12 27 C11 22 15 20 18 14 Z" fill="var(--gold)"/></svg>
  </div>
  <div class="band band--acts">BANDS <span class="star">★</span> BEER <span class="star">★</span> BBQ <span class="star">★</span> BOURBON</div>
  <div class="band band--host">HOSTED BY COPPERFIELD HOLLOW DISTILLERY</div>
  <div class="band band--address">2817 Marlow Pike Ashby, KY 40198</div>
</main>
</body>
</html>
```